Cork Lantern website design elements

Company: Cork Lantern
Business: Wine website (selling wine online)
www.corklantern.com.au
Please note that this is an initial project, ongoing design work will be required after this project.
Design requirement
Note: Full website design not required, only specific elements to enhance current design.
- Must work with existing logo and wood background (do not change site background)
- Must work with a orange (please improve current orange colour) and blue colour (blue colour in attachments)
- Pictures of wine bottles or wine glasses are not to be used in design elements.
I currently have an existing design which I would like certain elements designed for. Design elements must work with responsive functionality.
I am trying to achieve a modern retro feel of the website, please refer to the below websites as examples that I am trying to look like.
- https://au.pennytrimguild.com/
- http://www.harveykettle.com/italian/australia/home
- http://www.marigoldfizz.co.uk/
- http://www.netgather.org.nz/13/
As mentioned the site is already built and I need certain elements to work with what is already there. All elements must work with current logo and wood panel background.
I require the following elements
• Menu bar (must be the orange)
• Home page promo slider (Text, this weeks special etc)
• 2x homepage promo tabs buttons (Join the lantern club, what's in the box deal)
• 4x Homepage navigation tabs (Red wine, White wine, Sparkling, Pre mixed cases)
• Add to cart button
• Product image backdrop (can be wider than current examples)
o I would like the backdrops to be a different colour scheme to each other e.g red wine will habe red colour, white will have a cream colour, etc)
o I would prefer a close up of the product, does not need to be full view
Please refer to attachments for elements that I like and would like to mimic.
Colour scheme
- Use existing orange (please suggest if you think of a better tone)
- Secondary colour light baby blue (suggest best options)
- Please advise of other colours needed
Design elements to be provided in jog and raw design format.
This project will require ongoing work.
I will provide access details to site upon request.
Please contact me if you have any questions.
Rowan
Cork Lantern

```html
<!DOCTYPE html>
<html lang="en">
<head>
<meta charset="utf-8">
<title>Cork Lantern — Home</title>
<link rel="stylesheet" href="https://fonts.googleapis.com/css2?family=Alfa+Slab+One&family=Kaushan+Script&family=Oswald:wght@400;500&family=Josefin+Sans:wght@400;600&family=Josefin+Slab:wght@700&display=swap">
<style>
  :root {
    --wood-dark: #5a3c22;
    --wood-mid: #8a6440;
    --wood-light: #a98258;
    --orange: #e8682a;
    --paper: #f9f6ef;
    --nav-grey: #d8d8d5;
    --ink: #1c1a18;
    --brown: #3a2418;
    --gold: #8b7346;
    --sky: #cfe5ee;
    --steel-blue: #3d6577;
    --badge-blue: #8fb0cc;
    --tile-grey: #c7c7c4;
    --tile-text: #4a4a4a;
    --cream: #fbeee0;
  }
  * { box-sizing: border-box; margin: 0; padding: 0; }
  html, body { width: 1200px; height: 814px; overflow: hidden; }
  body { position: relative; font-family: "Oswald", sans-serif; color: var(--ink); }
  a { text-decoration: none; }

  .wood-backdrop {
    position: absolute; inset: 0;
    background: linear-gradient(90deg, var(--wood-mid), var(--wood-light) 30%, var(--wood-mid) 55%, var(--wood-light) 80%, var(--wood-dark));
  }
  .top-rule { position: absolute; left: 0; top: 0; width: 1200px; height: 6px; background: var(--orange); }

  .brand { position: absolute; left: 122px; top: 44px; display: flex; align-items: center; gap: 8px; }
  .brand-dot { width: 16px; height: 16px; border-radius: 50%; background: #fff; }
  .brand-name { font-family: "Alfa Slab One", serif; font-size: 22px; color: #fff; white-space: nowrap; }

  .search { position: absolute; left: 454px; top: 51px; width: 293px; height: 28px; background: #fff; display: flex; align-items: center; padding: 0 8px; font-family: Arial, sans-serif; font-size: 10px; color: #999; }
  .search svg { margin-left: auto; }

  .cart { position: absolute; left: 994px; top: 57px; display: flex; align-items: center; gap: 5px; font-family: Arial, sans-serif; font-size: 10px; color: #fff; white-space: nowrap; }

  .page { position: absolute; left: 98px; top: 114px; width: 1002px; height: 604px; background: var(--paper); }
  .page-top-band { position: absolute; left: 0; top: 0; width: 100%; height: 5px; background: var(--orange); }

  .main-nav { position: absolute; left: 0; top: 5px; width: 100%; height: 49px; background: var(--nav-grey); }
  .main-nav a { position: absolute; top: 0; height: 49px; line-height: 52px; font-family: "Alfa Slab One", serif; font-size: 15px; color: var(--ink); white-space: nowrap; }
  .main-nav a.is-active { width: 142px; text-align: center; background: var(--orange); color: #fff; outline: 1px dashed #fff; outline-offset: -4px; }

  .club-tag { position: absolute; left: 819px; top: 6px; width: 108px; height: 80px; }
  .club-tag-text { position: absolute; left: 0; top: 10px; width: 108px; text-align: center; font-family: "Alfa Slab One", serif; color: var(--cream); font-size: 14px; line-height: 17px; }
  .club-tag-text small { display: block; font-family: Arial, sans-serif; font-size: 10px; color: var(--ink); margin-top: 2px; }

  .promo-slider { position: absolute; left: 28px; top: 81px; width: 719px; height: 223px; background: var(--sky); border: 2px dotted #8a9aa8; overflow: hidden; }
  .promo-stamp { position: absolute; left: 12px; top: 32px; width: 152px; height: 132px; border-radius: 50%; background: #b9cdd5; }
  .promo-hand-right { position: absolute; left: 590px; top: 36px; width: 106px; height: 42px; background: #2a2a2a; border-radius: 4px; }
  .promo-hand-left { position: absolute; left: 48px; top: 156px; width: 92px; height: 40px; background: #2a2a2a; border-radius: 4px; }
  .promo-title { position: absolute; left: 150px; top: 6px; width: 450px; text-align: center; white-space: nowrap; font-family: "Alfa Slab One", serif; font-size: 128px; line-height: 130px; letter-spacing: 10px; color: var(--ink); text-shadow: 4px 4px 0 #fff; }
  .promo-sub { position: absolute; left: 150px; top: 128px; width: 450px; text-align: center; white-space: nowrap; font-family: "Kaushan Script", cursive; font-size: 64px; line-height: 72px; color: var(--gold); }

  .club-promo { position: absolute; left: 770px; top: 122px; width: 210px; text-align: center; white-space: nowrap; font-family: "Kaushan Script", cursive; font-size: 32px; line-height: 48px; color: var(--brown); }
  .join-btn { position: absolute; left: 790px; top: 248px; width: 160px; height: 34px; }
  .join-btn span { position: absolute; left: 0; top: 0; width: 150px; height: 34px; line-height: 35px; text-align: center; font-family: "Oswald", sans-serif; font-size: 20px; color: var(--cream); }

  .section-rule { position: absolute; top: 333px; display: flex; align-items: center; white-space: nowrap; }
  .section-rule h2 { font-family: "Kaushan Script", cursive; font-weight: 400; font-size: 26px; line-height: 32px; color: var(--steel-blue); margin: 0 14px; }

  .category-tile { position: absolute; top: 386px; width: 228px; height: 133px; background: var(--tile-grey); text-align: center; overflow: hidden; }
  .category-tile::before { content: ""; position: absolute; inset: 6px; border: 2px solid #f1f1ef; }
  .tile-title { position: absolute; left: 0; width: 100%; white-space: nowrap; font-family: "Josefin Sans", sans-serif; font-weight: 400; text-shadow: 1px 1px 0 #777; }
  .tile-link { position: absolute; left: 0; top: 98px; width: 100%; white-space: nowrap; font-family: "Oswald", sans-serif; font-size: 14px; color: var(--tile-text); letter-spacing: 0.5px; }
  .tile-red .tile-title { top: 36px; font-size: 40px; line-height: 44px; letter-spacing: 3px; color: #fff; }
  .tile-white .tile-title { top: 36px; font-size: 40px; line-height: 44px; letter-spacing: 3px; color: var(--orange); }
  .tile-sparkling .tile-title { top: 18px; font-size: 30px; line-height: 37px; letter-spacing: 2px; color: var(--badge-blue); font-weight: 600; }

  .choose-line { position: absolute; left: 774px; top: 408px; white-space: nowrap; font-family: "Josefin Slab", serif; font-weight: 700; font-size: 25px; line-height: 32px; color: var(--ink); }
  .mixed-badge { position: absolute; left: 870px; top: 382px; width: 110px; height: 110px; }
  .mixed-badge span { position: absolute; left: 0; top: 30px; width: 110px; text-align: center; font-family: "Alfa Slab One", serif; font-size: 18px; line-height: 26px; color: #fff; }

  .page-foot { position: absolute; left: 0; top: 586px; width: 100%; border-top: 2px dashed #e6cdbb; }
</style>
</head>
<body>
  <div class="wood-backdrop" role="img" aria-label="Rustic wood panel background"></div>
  <div class="top-rule"></div>

  <header>
    <div class="brand"><span class="brand-dot"></span><span class="brand-name">Cork Lantern</span></div>
    <div class="search">Search entire store here...
      <svg width="12" height="12" viewBox="0 0 12 12"><circle cx="5" cy="5" r="3.5" fill="none" stroke="#aaa" stroke-width="1.5"/><line x1="7.6" y1="7.6" x2="11" y2="11" stroke="#aaa" stroke-width="1.5"/></svg>
    </div>
    <div class="cart">
      <svg width="12" height="14" viewBox="0 0 12 14"><rect x="1" y="4" width="10" height="10" fill="#fff"/><path d="M4 4V2.5a2 2 0 0 1 4 0V4" fill="none" stroke="#fff" stroke-width="1.3"/></svg>
      Cart AU$0.00
    </div>
  </header>

  <main class="page">
    <div class="page-top-band"></div>
    <nav class="main-nav">
      <a href="#" style="left:60px">HOME</a>
      <a href="#" style="left:165px">RED WINE</a>
      <a href="#" class="is-active" style="left:272px">WHITE WINE</a>
      <a href="#" style="left:441px">SPARKLING</a>
      <a href="#" style="left:584px">MIXED CASES</a>
    </nav>

    <div class="club-tag">
      <svg width="108" height="80" viewBox="0 0 108 80"><polygon points="0,0 108,0 108,78 54,70 0,78" fill="#e8682a"/><polygon points="5,4 103,4 103,71 54,64 5,71" fill="none" stroke="#f4a878" stroke-dasharray="2 2"/></svg>
      <div class="club-tag-text">LANTERN<br>CLUB<small>see below</small></div>
    </div>

    <section class="promo-slider">
      <div class="promo-stamp" role="img" aria-label="Rubber stamp mark for premixed cases"></div>
      <div class="promo-hand-right" role="img" aria-label="Vintage pointing hand illustration"></div>
      <div class="promo-hand-left" role="img" aria-label="Vintage pointing hand illustration"></div>
      <div class="promo-title">THIS</div>
      <div class="promo-sub">weeks special</div>
    </section>

    <p class="club-promo">Join the<br>Lantern club</p>
    <a class="join-btn" href="#">
      <svg width="160" height="34" viewBox="0 0 160 34"><polygon points="0,0 140,0 160,17 140,34 0,34 12,17" fill="#e8682a"/></svg>
      <span>JOIN NOW</span>
    </a>

    <div class="section-rule" style="left:28px">
      <svg width="126" height="10" viewBox="0 0 130 10"><g fill="#3d6577" opacity=".8"><polygon points="0,0 6,5 0,10 4,10 10,5 4,0"/><polygon points="10,0 16,5 10,10 14,10 20,5 14,0"/><polygon points="20,0 26,5 20,10 24,10 30,5 24,0"/><polygon points="30,0 36,5 30,10 34,10 40,5 34,0"/><polygon points="40,0 46,5 40,10 44,10 50,5 44,0"/><polygon points="50,0 56,5 50,10 54,10 60,5 54,0"/><polygon points="60,0 66,5 60,10 64,10 70,5 64,0"/><polygon points="70,0 76,5 70,10 74,10 80,5 74,0"/><polygon points="80,0 86,5 80,10 84,10 90,5 84,0"/><polygon points="90,0 96,5 90,10 94,10 100,5 94,0"/><polygon points="100,0 106,5 100,10 104,10 110,5 104,0"/><polygon points="110,0 116,5 110,10 114,10 120,5 114,0"/><polygon points="120,0 126,5 120,10 124,10 130,5 124,0"/></g></svg>
      <h2>take control ~ mix your own case</h2>
      <svg width="126" height="10" viewBox="0 0 130 10"><g fill="#3d6577" opacity=".8"><polygon points="0,0 6,5 0,10 4,10 10,5 4,0"/><polygon points="10,0 16,5 10,10 14,10 20,5 14,0"/><polygon points="20,0 26,5 20,10 24,10 30,5 24,0"/><polygon points="30,0 36,5 30,10 34,10 40,5 34,0"/><polygon points="40,0 46,5 40,10 44,10 50,5 44,0"/><polygon points="50,0 56,5 50,10 54,10 60,5 54,0"/><polygon points="60,0 66,5 60,10 64,10 70,5 64,0"/><polygon points="70,0 76,5 70,10 74,10 80,5 74,0"/><polygon points="80,0 86,5 80,10 84,10 90,5 84,0"/><polygon points="90,0 96,5 90,10 94,10 100,5 94,0"/><polygon points="100,0 106,5 100,10 104,10 110,5 104,0"/><polygon points="110,0 116,5 110,10 114,10 120,5 114,0"/><polygon points="120,0 126,5 120,10 124,10 130,5 124,0"/></g></svg>
    </div>
    <div class="section-rule" style="left:748px">
      <h2>Can't decide?</h2>
      <svg width="52" height="10" viewBox="0 0 52 10"><g fill="#3d6577" opacity=".8"><polygon points="0,0 6,5 0,10 4,10 10,5 4,0"/><polygon points="10,0 16,5 10,10 14,10 20,5 14,0"/><polygon points="20,0 26,5 20,10 24,10 30,5 24,0"/><polygon points="30,0 36,5 30,10 34,10 40,5 34,0"/><polygon points="40,0 46,5 40,10 44,10 50,5 44,0"/></g></svg>
    </div>

    <a class="category-tile tile-red" href="#" style="left:28px"><span class="tile-title">RED</span><span class="tile-link">- SEE ALL RED WINES -</span></a>
    <a class="category-tile tile-white" href="#" style="left:273px"><span class="tile-title">WHITE</span><span class="tile-link">- SEE ALL WHITE WINES -</span></a>
    <a class="category-tile tile-sparkling" href="#" style="left:516px"><span class="tile-title">SWEET &amp;<br>SPARKLING</span><span class="tile-link">- SEE ALL SPARKLING WINES -</span></a>

    <p class="choose-line">Let us<br>choose<br>for you.</p>
    <a class="mixed-badge" href="#">
      <svg width="110" height="110" viewBox="0 0 110 110"><circle cx="55" cy="55" r="46" fill="#8fb0cc"/><circle cx="55" cy="55" r="49" fill="none" stroke="#8fb0cc" stroke-width="10" stroke-dasharray="8 6"/></svg>
      <span>MIXED<br>Case</span>
    </a>

    <div class="page-foot"></div>
  </main>
</body>
</html>
```